A poster for Vale Chiropractic's up coming powerful health workshop/seminar

I need a poster developed for Dr. Prent's upcoming Total Shape Reset and Armor Plating your Wellness seminar/workshop. This workshop will teach attendants how to shed pounds and rapidly reduce their waist size. Learn why weight loss doesn't work 99.9% of the time so that you can be the successful .1%. It's time to expose the LIES and reveal the TRUTH about the REAL causes of HEART DISEASE, DIABETES, CANCER, CHRONIC FATIGUE, ARTHRITIS, FIBROMYALGIA, and how to REVERSE/PREVENT this from ever happening to you or your family. The Insider Secrets to building your body into a health fortress unbreachable by sickness and disease. Learn to live and fufill your GOD-GIVEN health potential. Eliminate high bloodpressure, high cholesterol, diabetes, fatigue, chronic pain
Ending the WAR on sickness and disease by launching an unstoppable health offensive that will pummel any enemy of life and health.

I'm not a designer by any means, but was thinking of possible WAR theme, cammo, etc....just a thought. Not a requirement by any means
Updates

Dr. Prent has taken a look at all the submissions and has requested a few changes.

1. He wants the new map that has been added to the brief with Marlow Ridge College as a title above the map

2. He wants a section that describes what the attendees will gain at the seminar in bullet format.  Example:  Title....It's not about what you lose

                                                   I'ts about what you gain....

>The No-Hype, No- Gimmick  secrets for fast effective Weight loss

>How the top 3 disease killers, heart disease, cancer, and diabetes are linked to diet

>Tools and strategies to make 2012 the best year ever

The Seminar will be held at Marlow Ridge College, Tuesday January 3rd @ 6:30pm Open to Public

Target Market(s)

Adults 30-65

Industry/Entity Type

Building

Requirements
Should not have
• ruyrtur

```html
<!DOCTYPE html>
<html lang="en">
<head>
<meta charset="utf-8">
<title>Dr. Prent's Upcoming Seminar – Vale Chiropractic</title>
<link rel="stylesheet" href="https://fonts.googleapis.com/css2?family=Anton&family=Marcellus&family=Montserrat:wght@600;700&family=Open+Sans:ital,wght@1,600&display=swap">
<style>
  :root {
    --page: #ffffff;
    --frame-brown: #7a4a1e;
    --frame-dark: #4b2a10;
    --panel-dark: #2a1608;
    --gold: #e8b23a;
    --gold-deep: #b8801c;
    --headline-light: #f2c86a;
    --faint-word: rgba(150, 100, 60, 0.45);
    --banner-top: #c48a50;
    --banner-bottom: #9e6434;
    --banner-gold: #ffd21a;
    --banner-orange: #ffa21a;
    --bullet-text: #ffd64a;
    --alert-red: #e21a12;
  }
  * { margin: 0; padding: 0; box-sizing: border-box; }
  html, body { width: 930px; height: 1200px; overflow: hidden; background: var(--page); }
  .poster { position: relative; width: 930px; height: 1200px; }

  .frame {
    position: absolute; left: 62px; top: 64px; width: 811px; height: 1074px;
    background: radial-gradient(ellipse at 50% 55%, #8a5626 0%, var(--frame-brown) 55%, var(--frame-dark) 100%);
  }
  .feature-panel {
    position: absolute; left: 110px; top: 110px; width: 710px; height: 430px;
    background: linear-gradient(180deg, #1f1006 0%, var(--panel-dark) 55%, #4a2a12 100%);
  }

  .headline {
    position: absolute; left: 110px; top: 134px; width: 710px; text-align: center;
    font-family: "Anton", Impact, sans-serif; font-size: 50px; line-height: 54px;
    letter-spacing: 1px; text-transform: uppercase; white-space: nowrap;
    background: linear-gradient(180deg, var(--headline-light) 0%, var(--gold-deep) 100%);
    -webkit-background-clip: text; background-clip: text; color: transparent;
  }

  .disease-word {
    position: absolute; font-family: "Montserrat", Arial, sans-serif; font-weight: 700;
    text-transform: uppercase; white-space: nowrap; color: var(--faint-word);
  }
  .disease-word.is-gold { color: var(--gold); }
  .disease-word.is-pale { color: rgba(225, 210, 190, 0.8); }

  .casings {
    position: absolute; left: 250px; top: 300px; width: 520px; height: 220px;
    background: radial-gradient(ellipse at 60% 45%, rgba(214, 160, 40, 0.22) 0%, rgba(214, 160, 40, 0) 70%);
  }

  .seminar-banner {
    position: absolute; left: 110px; top: 530px; width: 710px; height: 172px;
    border-radius: 18px;
    background: linear-gradient(180deg, var(--banner-top) 0%, var(--banner-bottom) 100%);
  }
  .banner-copy {
    position: absolute; left: 218px; top: 542px; width: 490px; text-align: center;
    font-family: "Montserrat", Arial, sans-serif; font-weight: 700; white-space: nowrap;
  }
  .banner-copy .host { font-family: "Marcellus", Georgia, serif; font-weight: 400; font-size: 27px; line-height: 34px; color: var(--banner-gold); }
  .banner-copy .upcoming { font-size: 21px; line-height: 30px; color: var(--banner-gold); }
  .banner-copy .title { font-size: 21px; line-height: 27px; color: var(--banner-orange); font-weight: 600; }
  .banner-copy .amp { font-size: 19px; line-height: 20px; color: var(--banner-gold); }
  .banner-copy .title-end { font-size: 21px; line-height: 28px; color: var(--banner-gold); font-weight: 600; }

  .speaker-photo {
    position: absolute; left: 718px; top: 527px; width: 116px; height: 183px;
    background: linear-gradient(180deg, #8c6a52 0%, #5a3c2a 50%, #1e1e28 100%);
  }

  .gains {
    position: absolute; left: 80px; top: 718px; width: 770px; list-style: none; text-align: center;
    font-family: "Open Sans", Arial, sans-serif; font-style: italic; font-weight: 600;
    font-size: 15px; line-height: 31px; color: var(--bullet-text);
  }
  .gains li::before { content: "•"; margin-right: 8px; font-style: normal; }

  .venue-map {
    position: absolute; left: 351px; top: 813px; width: 284px; height: 212px;
    border: 3px solid #2a1a0c;
    background: linear-gradient(135deg, #8fa08a 0%, #c9cfc4 45%, #7e8e78 100%);
  }
  .map-marker { position: absolute; left: 441px; top: 826px; }

  .venue {
    position: absolute; left: 62px; top: 1036px; width: 811px; text-align: center;
    font-family: "Marcellus", Georgia, serif; color: var(--bullet-text); white-space: nowrap;
  }
  .venue .lead { font-size: 18px; line-height: 26px; }
  .venue .details { font-size: 18px; line-height: 30px; }
  .venue .college { font-size: 21px; font-weight: 700; }
</style>
</head>
<body>
<main class="poster">
  <div class="frame"></div>
  <div class="feature-panel"></div>

  <h1 class="headline">It's not about what you lose<br>It's about what you gain...</h1>

  <div class="casings" role="img" aria-label="Scattered brass bullet casings and bullet holes"></div>

  <span class="disease-word" style="left:204px;top:262px;font-size:24px;">Cancer</span>
  <span class="disease-word" style="left:541px;top:290px;font-size:24px;">Heart Disease</span>
  <span class="disease-word is-gold" style="left:275px;top:318px;font-size:28px;">Sickness</span>
  <span class="disease-word is-pale" style="left:598px;top:348px;font-size:17px;">Fibromyalgia</span>
  <span class="disease-word" style="left:213px;top:384px;font-size:28px;">Diabeties</span>
  <span class="disease-word is-gold" style="left:405px;top:414px;font-size:36px;">Diseases</span>
  <span class="disease-word" style="left:625px;top:462px;font-size:18px;">Arthritis</span>
  <span class="disease-word" style="left:305px;top:494px;font-size:24px;">Chronic Fatigue</span>

  <section class="seminar-banner"></section>
  <div class="banner-copy">
    <div class="host">Dr. Prent's</div>
    <div class="upcoming">UPCOMING</div>
    <div class="title">Total Shape Reset</div>
    <div class="amp">&amp;</div>
    <div class="title-end">Armor Plating your Wellness seminar</div>
  </div>
  <div class="speaker-photo" role="img" aria-label="Portrait photo of Dr. Prent in a suit and tie"></div>

  <ul class="gains">
    <li>The No-Hype, No-Gimmick secrets for fast effective Weight loss</li>
    <li>How the top 3 disease killers, heart disease, cancer, and diabetes are linked to diet.</li>
    <li>Tools and strategies to make 2012 the best year ever</li>
  </ul>

  <div class="venue-map" role="img" aria-label="Aerial map of Marlow Ridge College campus showing the auditorium"></div>
  <svg class="map-marker" width="136" height="34" viewBox="0 0 136 34" aria-label="Auditorium">
    <polygon points="0,17 22,2 22,9 136,9 136,25 22,25 22,32" fill="#e21a12"/>
    <text x="74" y="22" text-anchor="middle" font-family="Montserrat, Arial, sans-serif" font-weight="600" font-size="12" fill="#ffffff">Auditorium</text>
  </svg>

  <footer class="venue">
    <div class="lead">The Seminar will be held at</div>
    <div class="details"><span class="college">Marlow Ridge College,</span> Tuesday, January 3rd @ 6:30pm (Open to Public)</div>
  </footer>
</main>
</body>
</html>
```